Fresh-Up our Master Presentation

We are looking for someone who can revise our main presentation and make it more attractive. The previous layout and the slides are uploaded here and need to be revised. You are welcome to work with icons etc. here. The goal is to make it look a little more creative and modern. Brisk Otter is a company from the creative industry and therefore it would be great if it also shows this.

Target Market(s)

B2B

Industry/Entity Type

Communication and Content Creation

Font styles to use
Sans Serif

```html
<!DOCTYPE html>
<html lang="de">
<head>
<meta charset="utf-8">
<title>Brisk Otter – Präsentation</title>
<link href="https://fonts.googleapis.com/css2?family=Poppins:wght@400;500;600;700&family=Lora:wght@500&display=swap" rel="stylesheet">
<style>
:root{
  --navy:#2b3a55;
  --ink:#0f1c33;
  --text:#3b3f48;
  --paper:#ffffff;
  --bg:#ffffff;
  --line:#8c93a3;
}
*{margin:0;padding:0;box-sizing:border-box}
html,body{width:1200px;height:1111px;overflow:hidden;background:var(--bg)}
body{position:relative;font-family:'Poppins',sans-serif;color:var(--text)}
.slide{position:absolute;width:509px;height:286px;background:var(--paper);overflow:hidden;box-shadow:0 4px 16px rgba(0,0,0,.12)}
.s1{left:70px;top:77px}.s2{left:619px;top:77px}
.s3{left:70px;top:408px}.s4{left:619px;top:408px}
.s5{left:70px;top:739px}.s6{left:619px;top:739px}
.abs{position:absolute}
.brand{position:absolute;top:5px;right:6px;display:flex;align-items:center;gap:4px;font-weight:500;font-size:12px;color:var(--navy)}
.brand .dot{width:18px;height:18px;border-radius:50%;background:var(--navy)}
.title{position:absolute;font-weight:700;color:var(--navy);font-size:20px;line-height:1.1;text-align:center}
.rule{position:absolute;height:2px;background:var(--ink)}
.page{position:absolute;right:0;bottom:0;width:39px;height:17px;background:var(--navy);color:#fff;font-family:'Lora',serif;font-size:6px;display:flex;align-items:center;justify-content:center}
.photo{position:absolute}
.block{position:absolute;background:var(--navy)}
ul.bullets{position:absolute;list-style:none;font-size:7.6px;line-height:1.6}
ul.bullets li{position:relative;padding-left:10px;margin-bottom:9px;text-align:justify}
ul.bullets li::before{content:"";position:absolute;left:0;top:5px;width:3px;height:3px;border-radius:50%;background:var(--ink)}
.cover-bg{position:absolute;inset:0;background:linear-gradient(180deg,#f8ece2 0%,#ead9cf 35%,#c9a7a3 55%,#7d97a8 72%,#d96a3a 88%,#6b5f6a 100%)}
.cover-logo{position:absolute;left:125px;top:25px;display:flex;align-items:center;gap:8px;font-weight:500;font-size:38px;color:var(--navy)}
.cover-logo .dot{width:57px;height:57px;border-radius:50%;background:var(--navy)}
.cover-date{position:absolute;left:0;right:0;top:95px;text-align:center;font-family:'Lora',serif;font-size:16px;color:var(--navy)}
.hub{position:absolute;left:190px;top:92px;width:126px;height:126px;border-radius:50%;background:#041630;display:flex;align-items:center;justify-content:center;gap:5px;color:#fff;font-weight:500;font-size:14px}
.hub .dot{width:20px;height:20px;border-radius:50%;background:#fff}
.node{position:absolute;width:30px;height:30px;border:1px solid var(--navy);border-radius:3px}
.label{position:absolute;font-size:8px;font-weight:500;color:var(--ink);white-space:nowrap}
.label.left{text-align:right}
.disc{position:absolute;width:112px;height:112px;border-radius:50%;background:var(--navy)}
.phone{position:absolute;width:71px;height:147px;border:3px solid #0b1020;border-radius:10px}
.stats{position:absolute;font-size:8px;color:var(--text)}
.stats h3{font-size:10.5px;font-weight:600;color:var(--navy);margin-bottom:10px}
.stats ul{list-style:none}
.stats li{position:relative;padding-left:10px;margin-bottom:10px;line-height:1.25}
.stats li::before{content:"";position:absolute;left:1px;top:4px;width:3px;height:3px;border-radius:50%;background:var(--ink)}
.intro{position:absolute;left:170px;top:50px;width:170px;font-size:7.8px;line-height:1.55;text-align:justify;text-align-last:center}
.thumb{position:absolute;width:114px;height:109px;border:3px solid var(--navy)}
</style>
</head>
<body>

<section class="slide s1">
  <div class="cover-bg" role="img" aria-label="Low-poly pattern in cream, rose, blue and orange tones"></div>
  <div class="cover-logo"><span class="dot"></span>Brisk Otter</div>
  <p class="cover-date">Bern, 13. April 2023</p>
</section>

<section class="slide s2">
  <div class="brand"><span class="dot"></span>Brisk Otter</div>
  <h2 class="title" style="left:25px;top:50px;text-align:left">Jonas Weber und<br>Marc Keller</h2>
  <div class="rule" style="left:26px;top:98px;width:126px"></div>
  <ul class="bullets" style="left:26px;top:111px;width:238px">
    <li>Moderatoren, Podcaster, Social Media Hosts und DJs: Jonas Weber und Marc Keller sind schweizweit bekannte Persönlichkeiten mit hohem Unterhaltungswert</li>
    <li>Jonas Weber moderiert seit 20 Jahren und Marc Keller seit 10 Jahren Morgensendungen, insbesondere von Radio Pulse in der Schweiz. Als Morgenduo «Weber und Keller», mit dem Podcast «Die Plauderstunde» und mit verschiedenen Social Media-Formaten wie «Erst Freitag, wenn…» haben sie sich eine grosse Community aufgebaut.</li>
  </ul>
  <div class="block" style="left:286px;top:163px;width:90px;height:94px"></div>
  <div class="photo" style="left:297px;top:51px;width:203px;height:194px;background:linear-gradient(180deg,#b9c0c4,#6d7378 55%,#2c3036)" role="img" aria-label="Portrait of the two hosts standing with arms crossed above a city"></div>
  <div class="page">Page 02</div>
</section>

<section class="slide s3">
  <div class="brand"><span class="dot"></span>Brisk Otter</div>
  <h2 class="title" style="left:0;width:509px;top:6px">Die Community</h2>
  <div class="rule" style="left:191px;top:35px;width:127px"></div>
  <svg class="abs" style="left:0;top:0" width="509" height="286">
    <circle cx="253" cy="155" r="100" fill="none" stroke="var(--line)" stroke-width="0.8"/>
    <circle cx="253" cy="155" r="71" fill="#fff" stroke="var(--navy)" stroke-width="1"/>
  </svg>
  <div class="hub"><span class="dot"></span>Brisk Otter</div>
  <div class="node" style="left:163px;top:69px;background:linear-gradient(135deg,#c24a3a,#e2b36b)" role="img" aria-label="Radio show poster"></div>
  <div class="node" style="left:316px;top:69px;background:linear-gradient(135deg,#1c3d7a,#4d8fd0)" role="img" aria-label="Live moderation on stage"></div>
  <div class="node" style="left:140px;top:142px;background:linear-gradient(135deg,#e9e3da,#b0543d)" role="img" aria-label="Podcast cover artwork"></div>
  <div class="node" style="left:339px;top:142px;background:linear-gradient(135deg,#1b1e28,#4b5568)" role="img" aria-label="DJ performance"></div>
  <div class="node" style="left:163px;top:215px;background:linear-gradient(135deg,#8a5a4a,#d8b49c)" role="img" aria-label="Social media group photo"></div>
  <div class="node" style="left:316px;top:215px;background:linear-gradient(135deg,#23307a,#6b7fd6)" role="img" aria-label="TV studio set"></div>
  <span class="label left" style="right:350px;top:79px">Radio</span>
  <span class="label" style="left:351px;top:79px">Live-Moderation</span>
  <span class="label left" style="right:373px;top:152px">Podcast</span>
  <span class="label" style="left:374px;top:152px">DJ-Auftritte</span>
  <span class="label left" style="right:350px;top:225px">Social Media</span>
  <span class="label" style="left:351px;top:225px">TV-Moderation</span>
  <div class="page">Page 03</div>
</section>

<section class="slide s4">
  <div class="brand"><span class="dot"></span>Brisk Otter</div>
  <h2 class="title" style="left:0;width:509px;top:6px">Social Media-Präsenz</h2>
  <div class="rule" style="left:191px;top:35px;width:127px"></div>
  <div class="disc" style="left:2px;top:95px"></div>
  <div class="phone" style="left:23px;top:77px;background:linear-gradient(180deg,#c9cdd0,#d69a3a 60%,#2b2b2b)" role="img" aria-label="Phone showing a portrait in a yellow jacket"></div>
  <div class="stats" style="left:124px;top:82px;width:125px">
    <h3>Jonas Weber:</h3>
    <ul>
      <li>Pixgram: 48'700 Follower</li>
      <li>Friendbook: 29'200 Follower</li>
      <li>Posts zu den Themen Unterhaltung, Sport, Familie</li>
      <li>Auf Pixgram erreichte Konten pro Monat: 78'900</li>
      <li>Erreichte Zielgruppe: 53% Frauen / 46% Männer</li>
    </ul>
  </div>
  <div class="disc" style="left:257px;top:95px"></div>
  <div class="phone" style="left:278px;top:77px;background:linear-gradient(180deg,#a08a78,#3f3a33 55%,#d9d9d9 80%,#1e1e1e)" role="img" aria-label="Phone showing a portrait in a dark hooded jacket"></div>
  <div class="stats" style="left:376px;top:82px;width:125px">
    <h3>Jonas Weber:</h3>
    <ul>
      <li>Pixgram: 63'700 Follower</li>
      <li>Friendbook: 29'200 Follower</li>
      <li>Posts zu den Themen Unterhaltung, Motorrad, Sport</li>
      <li>Auf Pixgram erreichte Konten pro Monat: 140'600</li>
      <li>Erreichte Zielgruppe: 56% Frauen / 43% Männer</li>
    </ul>
  </div>
  <div class="page">Page 04</div>
</section>

<section class="slide s5">
  <div class="brand"><span class="dot"></span>Brisk Otter</div>
  <h2 class="title" style="left:0;width:509px;top:6px">Der Podcast</h2>
  <div class="rule" style="left:191px;top:35px;width:127px"></div>
  <div class="block" style="left:164px;top:169px;width:61px;height:93px"></div>
  <div class="photo" style="left:40px;top:55px;width:202px;height:194px;background:linear-gradient(160deg,#2a2f7a,#7a3fb0 40%,#c04a5a 70%,#1a1a2a)" role="img" aria-label="Live podcast show in a packed hall"></div>
  <ul class="bullets" style="left:270px;top:58px;width:206px;font-size:7.4px">
    <li>«Die Plauderstunde» gehört zu den Top 10-Podcasts auf Soundwave (Soundwave-Charts 2022) und ist der erfolgreichste Comedy Podcast der Schweiz.</li>
    <li>Seit 2019 sind über 200 Folgen des Podcasts erschienen. Sie wurden über 8 Millionen Mal gestreamt.</li>
    <li>Jede Folge wird von durchschnittlich 50'000 Menschen angehört!</li>
    <li>Der Podcast wurde bereits zwei Mal live vor jeweils 1'200 «Plauderer*innen» aufgezeichnet. Die beiden Shows waren in wenigen Sekunden restlos ausverkauft.</li>
    <li>Zum Podcast gehört eine Pixgram Seite mit fast 24'000 Abonnent*innen.</li>
  </ul>
  <div class="page">Page 05</div>
</section>

<section class="slide s6">
  <div class="brand"><span class="dot"></span>Brisk Otter</div>
  <h2 class="title" style="left:0;width:509px;top:6px">Vidtube-Content</h2>
  <div class="rule" style="left:191px;top:35px;width:127px"></div>
  <p class="intro">Seit vielen Jahren sind Jonas Weber und Marc Keller mit höchst erfolgreichen Vidtube-Formaten wie «Erst Freitag, wenn…», «Beni &amp; Res» oder «Mundart für Einsteiger» präsent. Ihr Vidtube Channel hat über 17'000 Abonnent*innen! Jonas Weber und Marc Keller gewannen 2022 zusammen mit dem Social Team von Pulse den «Alpine Comedy Prize».</p>
  <div class="thumb" style="left:23px;top:93px;background:linear-gradient(135deg,#8d8177,#e6ddd2 60%,#c23b2a)" role="img" aria-label="Video thumbnail of two hosts playing a block game"></div>
  <div class="thumb" style="left:199px;top:169px;background:linear-gradient(180deg,#6fb8e0,#1e8fd4 60%,#0d6fb8)" role="img" aria-label="Video thumbnail of friends jumping into a pool"></div>
  <div class="thumb" style="left:373px;top:93px;background:linear-gradient(180deg,#111 0 18%,#9aa1a8 18% 82%,#111 82%)" role="img" aria-label="Video thumbnail of a dialect quiz episode"></div>
  <div class="page">Page 06</div>
</section>

</body>
</html>
```